Window graphics for Kneadwell Haven

We need a new look for our store front. Attached is the current look and two samples of our logo.
the window measurements are (WxH in inches)
Top left: 72x32.5, each of the doors: 30x75.5, verical narrow window: 25.25x101, each of the two large windows on the right: 72x101

The new look will need to included the following content:

Content in each window:

Top left window: Our logo + 3817 (for the logo, try both short and long style)

Bottom left door: 614-555-0172 (don't make it too large. It must look clean and professional)

Right door: Logo

Vertical window right of right door: Every Day 10-9

Left large window:
Walk-Ins Welcome
Give the Gift of Massage!

Right large window:
Couples Massage
Hot Stone & Deep Tissue
Swedish & Foot

Target Market(s)

70% women, 30% men, middle class

Industry/Entity Type

Massage Center

Requirements
Must have
• A new fresh look to our store front. Easily read from a distance. The graphics and text must all be white only
Nice to have
• A clean look. See attached picture of a barber shop in our area.
Should not have
• Covering of whole window. Our landlord will not allow it.

```html
<!DOCTYPE html>
<html lang="en">
<head>
<meta charset="utf-8">
<title>Kneadwell Haven – Storefront Window Graphics</title>
<link rel="stylesheet" href="https://fonts.googleapis.com/css2?family=Courgette&family=Alfa+Slab+One&family=Lora:ital,wght@1,500&display=swap">
<style>
  :root {
    --awning: #ff1a5e;
    --trim-white: #ffffff;
    --wall: #d3d6da;
    --wall-shadow: #b3b4b8;
    --panel: #edb0a0;
    --panel-line: #a45a52;
    --frame: #2e2322;
    --kick: #5a4a43;
    --glass-light: #a7c4d0;
    --glass-dark: #668897;
    --sidewalk: #e0dfd2;
    --seam: #6e6e6e;
    --decal: #ffffff;
  }
  html, body { margin: 0; padding: 0; overflow: hidden; }
  body { width: 1200px; height: 1200px; background: var(--wall); }
  .storefront { display: block; width: 1200px; height: 1200px; }
  .script { font-family: "Courgette", cursive; fill: var(--decal); }
  .slab { font-family: "Alfa Slab One", serif; fill: var(--decal); }
  .serif-italic { font-family: "Lora", serif; font-style: italic; font-weight: 500; fill: var(--decal); }
  .flourish { fill: var(--decal); opacity: 0.35; }
</style>
</head>
<body>
<svg class="storefront" viewBox="0 0 1200 1200" xmlns="http://www.w3.org/2000/svg">
  <defs>
    <linearGradient id="glass" x1="1" y1="0" x2="0" y2="1">
      <stop offset="0" stop-color="var(--glass-light)"/>
      <stop offset="1" stop-color="#7ea0ae"/>
    </linearGradient>
    <pattern id="panel-seams" x="0" y="0" width="42.2" height="195" patternUnits="userSpaceOnUse">
      <rect width="42.2" height="195" fill="var(--panel)"/>
      <rect x="0" y="0" width="1" height="195" fill="var(--panel-line)"/>
    </pattern>
  </defs>

  <!-- fascia -->
  <rect class="awning" x="0" y="0" width="1200" height="190" fill="var(--awning)"/>
  <rect class="trim" x="0" y="190" width="1200" height="17" fill="var(--trim-white)"/>
  <rect class="wall" x="0" y="207" width="1200" height="357" fill="var(--wall)"/>
  <rect class="upper-panel" x="0" y="207" width="444" height="195" fill="url(#panel-seams)" stroke="var(--panel-line)" stroke-width="1"/>
  <rect class="upper-panel" x="530" y="207" width="626" height="195" fill="url(#panel-seams)" stroke="var(--panel-line)" stroke-width="1"/>
  <rect class="upper-panel-end" x="1156" y="207" width="44" height="195" fill="var(--panel)"/>
  <rect class="ledge-shadow" x="0" y="423" width="1200" height="2" fill="#a9abb0" opacity="0.7"/>
  <rect class="soffit" x="0" y="531" width="1200" height="33" fill="var(--wall-shadow)"/>

  <!-- left bay: frame and glass -->
  <rect class="frame" x="0" y="564" width="444" height="535" fill="var(--frame)"/>
  <rect class="glass transom" x="0" y="564" width="312" height="141" fill="url(#glass)"/>
  <polygon points="55,705 312,590 312,705" fill="var(--glass-dark)"/>
  <rect class="glass door" x="0" y="722" width="147" height="180" fill="url(#glass)"/>
  <polygon points="0,790 90,902 0,902" fill="var(--glass-dark)"/>
  <rect class="glass door" x="165" y="722" width="147" height="180" fill="url(#glass)"/>
  <polygon points="165,770 238,902 165,902" fill="var(--glass-dark)"/>
  <rect class="glass door" x="0" y="908" width="147" height="183" fill="var(--glass-dark)"/>
  <polygon points="0,908 55,908 147,1050 147,1091 0,1091" fill="#6d8f9d"/>
  <rect class="glass door" x="165" y="908" width="147" height="183" fill="var(--glass-dark)"/>
  <polygon points="225,908 312,908 312,1040" fill="#7a9cab"/>
  <rect class="glass narrow" x="328" y="564" width="116" height="462" fill="url(#glass)"/>
  <polygon points="328,690 444,876 444,1026 328,1026" fill="var(--glass-dark)"/>
  <rect class="kickplate" x="328" y="1033" width="116" height="58" fill="var(--kick)"/>

  <!-- pillar -->
  <rect class="pillar" x="444" y="564" width="86" height="535" fill="var(--wall)"/>

  <!-- right bay -->
  <rect class="frame" x="530" y="564" width="670" height="535" fill="var(--frame)"/>
  <rect class="glass large" x="530" y="564" width="329" height="462" fill="url(#glass)"/>
  <polygon points="530,564 812,1026 530,1026" fill="var(--glass-dark)"/>
  <rect class="glass large" x="871" y="564" width="329" height="462" fill="url(#glass)"/>
  <polygon points="871,564 1153,1026 871,1026" fill="var(--glass-dark)"/>
  <rect class="kickplate" x="530" y="1034" width="329" height="57" fill="var(--kick)"/>
  <rect class="kickplate" x="871" y="1034" width="329" height="57" fill="var(--kick)"/>

  <!-- sidewalk -->
  <rect class="sidewalk" x="0" y="1099" width="1200" height="101" fill="var(--sidewalk)"/>
  <line x1="530" y1="1099" x2="621" y2="1200" stroke="var(--seam)" stroke-width="1.2"/>
  <line x1="1124" y1="1099" x2="1200" y2="1146" stroke="var(--seam)" stroke-width="1.2"/>

  <!-- transom: name + number -->
  <g class="brand-name">
    <text class="script" x="155" y="640" font-size="34" text-anchor="middle">Kneadwell</text>
    <text class="script" x="178" y="676" font-size="34" text-anchor="middle">Haven</text>
  </g>
  <text class="script" x="73" y="750" font-size="23" text-anchor="middle">3817</text>

  <!-- gift certificate decal -->
  <g class="gift-decal">
    <rect x="22" y="776" width="104" height="81" fill="none" stroke="var(--decal)" stroke-width="0.8" opacity="0.8"/>
    <rect class="flourish" x="58" y="768" width="32" height="23" rx="4" role="img" aria-label="small ribbon bow ornament"/>
    <text class="slab" x="74" y="823" font-size="31" text-anchor="middle">Gift</text>
    <text class="slab" x="74" y="835" font-size="11.5" text-anchor="middle">Certificates</text>
    <text class="slab" x="74" y="847" font-size="11.5" text-anchor="middle">Available</text>
  </g>

  <!-- hours badge -->
  <g class="hours-badge">
    <circle cx="238" cy="813" r="48" fill="none" stroke="var(--decal)" stroke-width="0.9"/>
    <path id="arc-top" d="M 201 813 A 37 37 0 0 1 275 813" fill="none"/>
    <path id="arc-bottom" d="M 196 822 A 43 43 0 0 0 280 822" fill="none"/>
    <text class="serif-italic" font-size="15"><textPath href="#arc-top" startOffset="50%" text-anchor="middle">Every day</textPath></text>
    <text class="serif-italic" x="238" y="817" font-size="10.5" text-anchor="middle">10:00<tspan font-size="7">am</tspan> - 9:00<tspan font-size="7">pm</tspan></text>
    <text class="serif-italic" font-size="12"><textPath href="#arc-bottom" startOffset="50%" text-anchor="middle">614-555-0172</textPath></text>
  </g>

  <!-- large window decals -->
  <g class="service-decal">
    <rect class="flourish" x="620" y="616" width="148" height="22" rx="11" role="img" aria-label="scroll flourish ornament"/>
    <text class="script" x="694" y="666" font-size="25" text-anchor="middle">Walk-ins</text>
    <text class="script" x="694" y="692" font-size="25" text-anchor="middle">WELCOME</text>
    <rect class="flourish" x="620" y="702" width="148" height="22" rx="11" role="img" aria-label="scroll flourish ornament"/>
  </g>
  <g class="service-decal">
    <rect class="flourish" x="960" y="616" width="148" height="22" rx="11" role="img" aria-label="scroll flourish ornament"/>
    <text class="script" x="1034" y="666" font-size="25" text-anchor="middle">Swedish <tspan font-size="15">&amp;</tspan></text>
    <text class="script" x="1034" y="692" font-size="25" text-anchor="middle">Deep Tissue</text>
    <rect class="flourish" x="960" y="702" width="148" height="22" rx="11" role="img" aria-label="scroll flourish ornament"/>
  </g>
  <g class="service-decal">
    <rect class="flourish" x="622" y="864" width="148" height="22" rx="11" role="img" aria-label="scroll flourish ornament"/>
    <text class="script" x="695" y="914" font-size="25" text-anchor="middle">Sports</text>
    <text class="script" x="695" y="941" font-size="25" text-anchor="middle">Massage</text>
    <rect class="flourish" x="622" y="951" width="148" height="22" rx="11" role="img" aria-label="scroll flourish ornament"/>
  </g>
  <g class="service-decal">
    <rect class="flourish" x="960" y="864" width="148" height="22" rx="11" role="img" aria-label="scroll flourish ornament"/>
    <text class="script" x="1034" y="914" font-size="25" text-anchor="middle">Foot</text>
    <text class="script" x="1034" y="941" font-size="25" text-anchor="middle">Massage</text>
    <rect class="flourish" x="960" y="951" width="148" height="22" rx="11" role="img" aria-label="scroll flourish ornament"/>
  </g>
</svg>
</body>
</html>
```